VALTIRO.NET Single Product Based Website

We are one of the largest Stockiest of Diesel Engine (Marine and Power Plants) Spare Parts, this site will be focusing on a Single Product / Spare Parts - Connecting Rods <br/>We attached some actual pictures of the product and the Logo,<br/><br/>Once we approved your design shall provide with some contends and 10 actual Pictures to be added , should be a single page website SEO friendly sources to be used<br/>Should be Desktop, laptop and mobile friendly <br/><br/>best regards<br/>Oliver <br/>

Coding

Coded - Design and coding required

Number of Pages Required

1 page

Font styles to use
Other font styles liked:
• Book Antigua, Book Man Old Style or the designer can suggest

Colors

Designer to choose colors to be used in the design.

Requirements
Must have
• The Logo and same theme / colors can be used
Nice to have
• We shall provide the actual pictures of the product from our gallery approx 10 pictures to be added at final stage
Should not have
• other than initial design purpose , do not use any pictures downloaded from the internet

```html
<!DOCTYPE html>
<html lang="en">
<head>
<meta charset="utf-8">
<title>VALTIRO.NET — Connecting Rods</title>
<link href="https://fonts.googleapis.com/css2?family=Montserrat:wght@400;500;600;700&family=PT+Serif:ital,wght@0,700;1,400&display=swap" rel="stylesheet">
<style>
:root{
  --blue:#2d4f8e;
  --blue-deep:#1f3f80;
  --orange:#e4533a;
  --red:#d7392f;
  --ink:#222;
  --light:#f1f1f1;
  --dark:#0b0c0f;
  --field:#1b1c20;
  --white:#fff;
}
*{margin:0;padding:0;box-sizing:border-box}
html,body{width:1200px;height:2314px;overflow:hidden}
body{font-family:"Montserrat",sans-serif;color:var(--ink);background:var(--white);position:relative}
.serif{font-family:"PT Serif",Georgia,serif}
.abs{position:absolute}
.logo{font-family:"Montserrat",sans-serif;font-weight:700;font-size:21px;letter-spacing:.5px;display:flex;align-items:center;gap:8px}
.logo .dot{width:10px;height:10px;border-radius:50%;background:currentColor}
.pill{display:flex;align-items:center;justify-content:center;width:133px;height:40px;border-radius:20px;background:var(--blue);color:var(--white);font-size:12px;font-weight:600;letter-spacing:.3px;box-shadow:0 3px 8px rgba(0,0,0,.25)}

/* hero */
.hero{top:0;left:0;width:1200px;height:537px;background:linear-gradient(100deg,#c8302c 0%,#8d2f4e 35%,#3e2f72 62%,#1e3579 100%)}
.hero .logo{left:202px;top:50px;color:var(--white)}
.nav{right:205px;top:41px;display:flex;gap:26px;color:var(--white);font-size:12.5px;font-weight:600}
.hero h1{left:202px;top:174px;color:var(--white);font-size:44px;line-height:46px;font-weight:400}
.hero h1 b{font-weight:700}
.hero p{left:202px;top:284px;width:480px;color:var(--white);font-size:14.3px;line-height:21.3px}
.hero .pill{left:203px;top:404px}
.hero-art{left:690px;top:110px;width:385px;height:345px;border-radius:40px;background:radial-gradient(ellipse at center,#b9bcc4 0%,#7c8090 55%,rgba(60,60,100,0) 75%)}

/* intro */
.intro{top:537px;left:0;width:1200px;height:358px;background:var(--white)}
.map{left:30px;top:30px;width:1140px;height:320px;background:radial-gradient(ellipse at center,#f1f1f3 0%,#fafafa 60%,#fff 80%)}
.intro h2{left:202px;top:70px;font-size:38px;line-height:36px;color:var(--blue)}
.intro h2 span{color:var(--orange)}
.intro p{left:203px;top:165px;width:420px;font-size:12.6px;line-height:17px;color:#333}
.intro-art{left:665px;top:88px;width:330px;height:215px;border-radius:30px;background:linear-gradient(135deg,#e4e5e8,#9fa2a9 60%,#cfd1d5)}

/* products */
.products{top:895px;left:0;width:1200px;height:757px;background:var(--light)}
.products h2{left:0;width:1200px;top:28px;text-align:center;font-size:34px;color:var(--blue)}
.products h2 span{color:var(--orange)}
.products .lead{left:270px;top:87px;width:660px;text-align:center;font-size:13.8px;line-height:21.7px;color:#333}
.grid{left:202px;top:191px;display:grid;grid-template-columns:repeat(3,250px);grid-auto-rows:209px;gap:21px 22px}
.shot{display:block}
.s1{background:linear-gradient(135deg,#8d8d8f,#b7b8ba 50%,#7c7c7e)}
.s2{background:linear-gradient(180deg,#6b645d,#a8a39d 50%,#5e5852)}
.s3{background:linear-gradient(135deg,#cfc2ad,#a4a3a2 50%,#d3c5ae)}
.s4{background:linear-gradient(135deg,#7e7f82,#b4b5b8 55%,#838487)}
.s5{background:linear-gradient(135deg,#e8c438,#7f8a9a 50%,#e7c035)}
.s6{background:linear-gradient(135deg,#6c6258,#b9b4ae 55%,#7c6f62)}
.products .pill{left:534px;top:674px}

/* band */
.band{top:1652px;left:0;width:1200px;height:259px;background:linear-gradient(180deg,#24478e,#1f3f83);color:var(--white);text-align:center}
.band .kicker{left:0;width:1200px;top:50px;font-size:33px;font-style:italic;font-weight:400}
.band h3{left:0;width:1200px;top:99px;font-size:35px;font-weight:700}
.band p{left:270px;width:660px;top:157px;font-size:13.8px;line-height:21.7px}

/* contact */
.contact{top:1911px;left:0;width:1200px;height:403px;background:var(--dark);color:var(--white)}
.contact h2{left:0;width:1200px;top:30px;text-align:center;font-size:34px;color:var(--orange)}
.contact h2 span{color:var(--blue)}
.contact .sub{left:202px;top:68px;font-size:18.5px;font-weight:600}
.field{height:42px;background:var(--field);border:1px solid #222;color:#aaa;font-size:11.5px;display:flex;align-items:center;padding-left:11px}
.f-name{left:202px;top:106px;width:257px}
.f-email{left:473px;top:106px;width:257px;padding-left:17px}
.f-phone{left:740px;top:106px;width:256px;padding-left:13px}
.f-msg{left:202px;top:163px;width:665px;padding-left:13px}
.submit{left:880px;top:163px;width:116px;height:42px;border:2px solid var(--orange);display:flex;align-items:center;justify-content:center;font-weight:700;font-size:14px}
.contact .logo{left:202px;top:228px;color:var(--blue)}
.social{left:204px;top:300px;display:flex;gap:11px}
.social i{width:30px;height:30px;border-radius:50%;display:block}
.office{top:253px;font-size:11.3px;line-height:15.5px}
.office h4{color:var(--orange);font-weight:500;font-size:12.5px;margin-bottom:6px}
.office p+p{margin-top:15px}
.o1{left:424px}.o2{left:631px}.o3{left:837px}
.rule{left:0;top:361px;width:1200px;height:1px;background:var(--orange)}
.copy{left:0;width:1200px;top:375px;text-align:center;font-size:12.5px}
</style>
</head>
<body>

<header class="hero abs">
  <div class="logo abs"><span class="dot"></span>VALTIRO.NET</div>
  <nav class="nav abs"><span>Home</span><span>About</span><span>Features</span><span>Product</span><span>Reviews</span><span>Faq</span><span>Contact</span></nav>
  <h1 class="abs">A <b>connecting rod,</b><br>also called a <b>con rod</b></h1>
  <p class="abs"><b>connecting rod</b>, is the part of a piston engine which connects the piston to the crankshaft. Together with the crank, the connecting rod converts the reciprocating motion of the piston into the rotation of the crankshaft.</p>
  <span class="pill abs">LEARN MORE</span>
  <div class="hero-art abs" role="img" aria-label="Rendered crankshaft assembly with four pistons and connecting rods"></div>
</header>

<section class="intro abs">
  <div class="map abs" role="img" aria-label="Faint dotted world map background"></div>
  <h2 class="abs serif">Internal combustion<br><span>engines</span></h2>
  <p class="abs">A connecting rod for an internal combustion engine consists of the 'big end', 'rod' and 'small end'. The small end attaches to the gudgeon pin (also called 'piston pin' or 'wrist pin'), which can swivel in the piston. Typically, the big end connects to the crankpin using a plain bearing to reduce friction; however some smaller engines may instead use a rolling-element bearing, in order to avoid the need for a pumped lubrication system</p>
  <div class="intro-art abs" role="img" aria-label="Single piston attached to a connecting rod"></div>
</section>

<section class="products abs">
  <h2 class="abs serif"><span>Our</span> Products</h2>
  <p class="lead abs">It’s more than likely someone you know or race against runs Ardent billet aluminum connecting rods and oil pumps that can be found in top-performing engines and race cars around the world. Now it’s your turn to join the ranks of the best.</p>
  <div class="grid abs">
    <span class="shot s1" role="img" aria-label="Polished connecting rod on grey surface"></span>
    <span class="shot s2" role="img" aria-label="Rows of used connecting rods"></span>
    <span class="shot s3" role="img" aria-label="Two labelled connecting rods on cardboard"></span>
    <span class="shot s4" role="img" aria-label="Connecting rod lying flat on grey surface"></span>
    <span class="shot s5" role="img" aria-label="Three numbered connecting rods on yellow cloth"></span>
    <span class="shot s6" role="img" aria-label="Close-up of a stamped connecting rod big end"></span>
  </div>
  <span class="pill abs">VIEW MORE</span>
</section>

<section class="band abs" role="img" aria-label="Blue tinted engine parts background">
  <p class="kicker abs serif">Internal combustion engines</p>
  <h3 class="abs">connecting rod for an internal combustion engine.</h3>
  <p class="abs">Typically there is a pinhole bored through the bearing on the big end of the connecting rod so that lubricating oil squirts out onto the thrust side of the cylinder wall to lubricate.</p>
</section>

<footer class="contact abs">
  <h2 class="abs serif">Get in <span>Touch</span></h2>
  <p class="sub abs">Send us a message</p>
  <div class="field abs f-name">Name</div>
  <div class="field abs f-email">Email</div>
  <div class="field abs f-phone">Phone</div>
  <div class="field abs f-msg">Message</div>
  <div class="submit abs">SUBMIT</div>

  <div class="logo abs"><span class="dot"></span>VALTIRO.NET</div>
  <div class="social abs">
    <i style="background:#2d4f8e"></i><i style="background:#2b62c4"></i><i style="background:#e4533a"></i><i style="background:#d8335c"></i>
  </div>

  <div class="office abs o1"><h4>NEW YORK</h4><p>27 Harlow Rd #12, Brenford, CA,<br>95011 - Newyork</p><p>+44 800 555 10<br>info@valtiro.net</p></div>
  <div class="office abs o2"><h4>LONDON</h4><p>31 Harlow Rd #12, Brenford, CA,<br>95011 - London</p><p>+44 800 555 20<br>info@valtiro.net</p></div>
  <div class="office abs o3"><h4>MADRID</h4><p>19 Harlow Rd #12, Brenford, CA,<br>95011 - Madrid</p><p>+44 820 555 30<br>info@valtiro.net</p></div>

  <div class="rule abs"></div>
  <p class="copy abs">Copyright 2018 valtiro.net - All Rights Reserved</p>
</footer>

</body>
</html>
```